Brochure and Flyer template, Aluminium Facade company
Verdantis Structural Concepts pty Ltd
We are looking for a cutting edge Brochure and Flyer template that we can change text and pictures for different marketing products and services we provide to different target markets and audiences. We like a mixture of A4 size but also like the A5 size so please feel free to be creative.
Construction
Corporate, Building Companies, Architects, Home owners.
We are needing the Brochure template to cater for multiple product pictures and descriptions in either A4 or A5 format (please be creative) and the flier template is more aimed to focus on 1 or 2 individual products.
1 of 2 files of Past project photos for your use if you like
Our Logo
Our Logo Different Format
Our Company Profile (old and out dated for reference only!)
2 of 2 files of Past project photos for your use if you like
Past Projects for information on our company
SOME of our standard Products FOR YOUR INFORMATION ONLY
Havenor opening roof System Photos to go with the operable section Please make sure the Havenor logo is used
Our Products and Services description
Havenor opening Roof information
More Havenor opening roof pics and data. May be of use

```html
<!DOCTYPE html>
<html lang="en">
<head>
<meta charset="utf-8">
<title>Verdantis Brochure Spread – Blades</title>
<link href="https://fonts.googleapis.com/css2?family=Open+Sans:wght@400;600;700&family=Roboto+Condensed:ital,wght@0,700;1,700&display=swap" rel="stylesheet">
<style>
  :root{
    --bg:#e4e5e5;
    --paper:#ffffff;
    --green:#3b9160;
    --green-dark:#1e6a45;
    --mint:#d8e8de;
    --grey-swoosh:#cfd3d2;
    --text:#5d6462;
    --photo-sky:#a9c4d6;
    --photo-wood:#b89a72;
    --louvre-dark:#3a3533;
    --louvre-mid:#6e6865;
  }
  *{box-sizing:border-box;margin:0;padding:0}
  html,body{width:1200px;height:799px;overflow:hidden;background:var(--bg);font-family:"Open Sans",Arial,sans-serif}
  .spread{position:absolute;left:40px;top:20px;width:1120px;height:759px;display:flex;box-shadow:0 6px 24px rgba(0,0,0,.18)}
  .page{position:relative;width:560px;height:759px;background:var(--paper);overflow:hidden}
  .page--left{border-right:1px solid #e2e2e2}
  .deco{position:absolute;inset:0;width:100%;height:100%}
  .deco--front{z-index:1}
  .heading{position:absolute;font-family:"Roboto Condensed",Arial,sans-serif;font-weight:700;color:var(--green);text-transform:uppercase;letter-spacing:.5px;white-space:nowrap}
  .page--left .heading{left:200px;top:34px;font-size:24px}
  .page--right .heading{right:40px;top:70px;font-size:28px;font-style:italic}
  .photo{position:absolute}
  .photo-grid{position:absolute;left:120px;top:78px;width:280px;height:220px;display:grid;grid-template-columns:60px 1fr 1fr;grid-template-rows:1fr 1fr;gap:5px}
  .photo-grid .photo{position:static;background:linear-gradient(160deg,var(--photo-sky),var(--photo-wood))}
  .photo-product{left:410px;top:24px;width:100px;height:84px;background:linear-gradient(135deg,#9aa0a6,#4b5157)}
  .body-copy{position:absolute;font-size:12px;line-height:1.55;color:var(--text)}
  .body-copy p{margin-bottom:12px}
  .page--left .body-copy{left:42px;top:325px;width:270px}
  .page--right .body-copy{left:215px;top:140px;width:305px}
  .signoff{position:absolute;left:300px;top:585px;font-size:12px;color:var(--green)}
  .footer-note{position:absolute;font-size:10px;color:#fff;z-index:2}
  .page--left .footer-note{left:40px;top:690px}
  .page--right .footer-note{left:40px;top:722px}
  .brand{position:absolute;display:flex;align-items:center;gap:6px;color:#fff;font-weight:700;font-size:14px;letter-spacing:1px;text-transform:uppercase;z-index:2}
  .brand__dot{width:16px;height:16px;border-radius:50%;background:#fff}
  .page--left .brand{left:110px;top:650px}
  .page--right .brand{right:40px;top:712px}
  .photo-louvre{left:40px;top:300px;width:320px;height:390px;background:linear-gradient(120deg,var(--louvre-dark),var(--louvre-mid) 55%,var(--louvre-dark))}
  .photo-circle{left:385px;top:360px;width:140px;height:140px;border-radius:50%;background:linear-gradient(160deg,var(--photo-sky),#6f7d80);border:5px solid #fff;box-shadow:0 0 0 1px #ccc}
</style>
</head>
<body>
<div class="spread">
  <section class="page page--left">
    <svg class="deco" viewBox="0 0 560 759" aria-hidden="true">
      <path d="M0 0 H230 C150 40 110 120 100 260 C60 180 20 120 0 110 Z" fill="var(--grey-swoosh)"/>
      <path d="M0 640 C180 610 380 640 560 600 V759 H0 Z" fill="var(--green)"/>
      <path d="M0 690 C200 660 400 700 560 650 V759 H0 Z" fill="var(--green-dark)"/>
    </svg>
    <h2 class="heading">Elliptical Blades</h2>
    <div class="photo photo-product" role="img" aria-label="Rendered elliptical blade profile"></div>
    <div class="photo-grid">
      <div class="photo" role="img" aria-label="Project photo of blade facade detail"></div>
      <div class="photo" role="img" aria-label="Project photo of elliptical blade awning"></div>
      <div class="photo" role="img" aria-label="Project photo of covered outdoor area"></div>
      <div class="photo" role="img" aria-label="Project photo of blade screen detail"></div>
      <div class="photo" role="img" aria-label="Project photo of pergola with blades"></div>
      <div class="photo" role="img" aria-label="Project photo of timber look blade roof"></div>
    </div>
    <div class="body-copy">
      <p>Slim elliptical blades shape daylight and airflow across every facade, keeping interiors cool while framing clear views outward.</p>
      <p>Each profile is extruded from marine grade aluminium and finished in durable powder coat colours to suit any project.</p>
      <p>Fixed or operable, blades mount to standard brackets for fast install.</p>
    </div>
    <div class="signoff">John Doe, ABC</div>
    <div class="brand"><span class="brand__dot"></span>Verdantis</div>
    <div class="footer-note">© 2013 Verdantis Structural Concepts pty Ltd</div>
  </section>

  <section class="page page--right">
    <svg class="deco" viewBox="0 0 560 759" aria-hidden="true">
      <path d="M150 0 H560 V360 C470 300 330 260 250 180 C200 130 170 70 150 0 Z" fill="var(--mint)"/>
      <path d="M200 118 C300 108 420 110 530 120" fill="none" stroke="var(--green)" stroke-width="4"/>
    </svg>
    <h2 class="heading">Ventilation Louvre Blades</h2>
    <div class="body-copy">
      <p>Ventilation louvre blades keep rain out and let fresh air through, ideal for plant rooms, car parks and screening walls.</p>
      <p>Blades are spaced to suit each site and can be made to length, angle and colour on request.</p>
    </div>
    <div class="photo photo-louvre" role="img" aria-label="Product photo of dark ventilation louvre blades"></div>
    <div class="photo photo-circle" role="img" aria-label="Project photo of louvre roof from below"></div>
    <svg class="deco deco--front" viewBox="0 0 560 759" aria-hidden="true">
      <path d="M0 700 C200 680 380 710 560 680 V759 H0 Z" fill="var(--green)"/>
    </svg>
    <div class="footer-note">© 2013 Verdantis Structural Concepts pty Ltd</div>
    <div class="brand"><span class="brand__dot"></span>Verdantis</div>
  </section>
</div>
</body>
</html>
```